Bramwell Garden Maintenance - Needs a business card! Easy JOB!

I need a business card for a new company called Bramwell Garden Maintenance. I will be offering the below services.

I am relatively open for ideas, so please be at your creative best.

I think I will list all the services offered on the rear of the card.

- Gardening
- Lawn Care
- Hedge Trimming
- Rubbish Removal
- Weeding/Spraying
- Landscaping
- Gutter Cleaning
- Solar Panel Cleaning
- Irrigation
- Pruning
- On-Site Mulching
- Ask for other services

I am still a little undecided on the colours. I prefer the logos with the Blue text, but I am open for ideas ( the logo/texts colours are not final).

Please use the catch phrase "What can Bramwell do for you?"

Here are the required details.

Bramwell Garden Maintenance

Neil Harcourt (owner)
Ph: 1300 XXX XXX
Mob: 0427 XXX XXX

neil@bramwellgarden.com.au
www.bramwellgarden.com.au
facebook.com/BramwellGarden
twitter.com/BramwellGarden
ABN: XXX XXX XXX ( this can be in smaller text somewhere, this is the least important )

Thankyou in advance! And good luck.

regards,
Neil
Updates

Hi everyone, please make sure you include the phrase "What can Bramwell do for you?" on the designs.

thanks,
Neil

Definitely liking the focus on a majority of the design on the blue colour from the logo. Also a splash of green in the plant.

Please make sure you list the services provided on the rear of the card. thanks.

With the service listing, please make "ask for other services" stand out, either a different colour or position or size... as long as it is more noticeable than the other services listed. Thanks.

Industry/Entity Type

Business

Requirements
Must have
• - use the font supplied (Brandon Family Font)
- use of the catch phrase "What can Bramwell do for you?"
- Double sided design
- Socialhub and Chirper logos/links
- Please use symbol/picture for "phone" "mobile" "email" instead of using the words.
- List the services provided on the rear of the card

```html
<!DOCTYPE html>
<html lang="en">
<head>
<meta charset="utf-8">
<title>Bramwell Garden Maintenance – Business Card</title>
<link href="https://fonts.googleapis.com/css2?family=Jost:wght@400;500;600&display=swap" rel="stylesheet">
<style>
  :root {
    --page-bg: #e6e4e0;
    --card-dark: #3a3b3e;
    --card-darker: #2f3033;
    --band-blue: #2340b4;
    --band-blue-deep: #1a2c8c;
    --logo-blue: #2f8fd8;
    --text-light: #f2f3f5;
    --text-soft: #d9dbe0;
    --divider: #1f2022;
    --icon-blue: #3d9be0;
  }
  * { box-sizing: border-box; margin: 0; padding: 0; }
  html, body {
    width: 1200px;
    height: 900px;
    overflow: hidden;
    background: var(--page-bg);
    font-family: "Jost", "Helvetica Neue", Arial, sans-serif;
  }
  .canvas {
    position: relative;
    width: 1200px;
    height: 900px;
  }
  .card {
    position: absolute;
    left: 290px;
    width: 620px;
    height: 379px;
    border-radius: 4px;
    background: linear-gradient(160deg, var(--card-dark), var(--card-darker));
    box-shadow: 0 6px 18px rgba(0,0,0,0.25);
    overflow: hidden;
    color: var(--text-light);
  }
  .card--back { top: 51px; }
  .card--front { top: 470px; }

  /* Back side */
  .tagline-band {
    height: 72px;
    background: linear-gradient(180deg, var(--band-blue), var(--band-blue-deep));
    display: flex;
    align-items: center;
    padding-left: 34px;
  }
  .tagline {
    font-size: 33px;
    font-weight: 500;
    color: var(--text-light);
    letter-spacing: 0.2px;
  }
  .services {
    display: flex;
    padding: 30px 0 0 62px;
  }
  .service-list {
    list-style: none;
    width: 268px;
  }
  .service-list li {
    font-size: 21px;
    line-height: 40px;
    color: var(--text-soft);
    position: relative;
    padding-left: 18px;
  }
  .service-list li::before {
    content: "";
    position: absolute;
    left: 0;
    top: 17px;
    width: 6px;
    height: 6px;
    border-radius: 50%;
    background: var(--text-light);
  }

  /* Front side */
  .brand-block {
    position: absolute;
    left: 0;
    top: 0;
    width: 285px;
    height: 100%;
    display: flex;
    flex-direction: column;
    align-items: center;
    justify-content: center;
  }
  .brand-mark {
    width: 74px;
    height: 74px;
    border-radius: 50%;
    background: var(--logo-blue);
    margin-bottom: 18px;
  }
  .brand-name {
    font-weight: 600;
    color: var(--logo-blue);
    text-align: center;
    text-transform: uppercase;
    line-height: 1;
  }
  .brand-name__main {
    display: block;
    font-size: 44px;
    letter-spacing: 1px;
  }
  .brand-name__sub {
    display: block;
    font-size: 15px;
    letter-spacing: 1.5px;
    margin-top: 6px;
  }
  .divider {
    position: absolute;
    left: 285px;
    top: 70px;
    width: 2px;
    height: 240px;
    background: var(--divider);
    box-shadow: 1px 0 0 rgba(255,255,255,0.06);
  }
  .contact {
    position: absolute;
    left: 318px;
    top: 40px;
  }
  .contact__name {
    font-size: 20px;
    font-weight: 600;
    margin-bottom: 4px;
  }
  .contact__role { font-weight: 400; }
  .contact__phones { margin-bottom: 40px; }
  .contact-line {
    display: flex;
    align-items: center;
    gap: 8px;
  }
  .contact-line--phone {
    font-size: 20px;
    line-height: 30px;
  }
  .contact-line--small {
    font-size: 15px;
    line-height: 23px;
  }
  .contact-line svg { flex: none; }
  .contact__abn {
    font-size: 15px;
    line-height: 23px;
    padding-left: 20px;
  }
</style>
</head>
<body>
<div class="canvas">

  <section class="card card--back" aria-label="Card back: services">
    <div class="tagline-band">
      <h2 class="tagline">What can Bramwell do for you?</h2>
    </div>
    <div class="services">
      <ul class="service-list">
        <li>Gardening</li>
        <li>Lawn Care</li>
        <li>Hedge Trimming</li>
        <li>Rubbish Removal</li>
        <li>Weeding/Spraying</li>
        <li>Landscaping</li>
      </ul>
      <ul class="service-list">
        <li>Gutter Cleaning</li>
        <li>Solar Panel Cleaning</li>
        <li>Irrigation</li>
        <li>Pruning</li>
        <li>On-Site Mulching</li>
        <li>Ask for other services</li>
      </ul>
    </div>
  </section>

  <section class="card card--front" aria-label="Card front: contact details">
    <div class="brand-block">
      <span class="brand-mark"></span>
      <h1 class="brand-name">
        <span class="brand-name__main">Bramwell</span>
        <span class="brand-name__sub">Garden Maintenance</span>
      </h1>
    </div>
    <div class="divider"></div>
    <div class="contact">
      <p class="contact__name">Neil Harcourt <span class="contact__role">owner</span></p>
      <div class="contact__phones">
        <p class="contact-line contact-line--phone">
          <svg width="12" height="16" viewBox="0 0 12 16" aria-label="Phone"><path d="M3 1 L5 1 L6 4.5 L4.5 5.5 Q5.5 9 7.5 10.5 L9 9.5 L11 12 L9.5 14.5 Q2 12 1.5 3 Z" fill="var(--icon-blue)"/></svg>
          1300 XXX XXX
        </p>
        <p class="contact-line contact-line--phone">
          <svg width="12" height="16" viewBox="0 0 12 16" aria-label="Mobile"><rect x="2" y="1" width="8" height="14" rx="1.5" fill="var(--icon-blue)"/><rect x="3.3" y="3" width="5.4" height="8" fill="var(--card-dark)"/></svg>
          0427 XXX XXX
        </p>
      </div>
      <p class="contact-line contact-line--small">
        <svg width="13" height="10" viewBox="0 0 13 10" aria-label="Email"><rect x="0.5" y="0.5" width="12" height="9" fill="var(--icon-blue)"/><path d="M0.5 0.5 L6.5 5.5 L12.5 0.5" stroke="var(--card-dark)" stroke-width="1" fill="none"/></svg>
        neil@bramwellgarden.com.au
      </p>
      <p class="contact-line contact-line--small">
        <svg width="12" height="12" viewBox="0 0 12 12" aria-label="Website"><circle cx="6" cy="6" r="5.3" fill="none" stroke="var(--icon-blue)" stroke-width="1.2"/><ellipse cx="6" cy="6" rx="2.3" ry="5.3" fill="none" stroke="var(--icon-blue)" stroke-width="1"/><line x1="0.7" y1="6" x2="11.3" y2="6" stroke="var(--icon-blue)" stroke-width="1"/></svg>
        www.bramwellgarden.com.au
      </p>
      <p class="contact-line contact-line--small">
        <svg width="12" height="12" viewBox="0 0 12 12" aria-hidden="true"><rect width="12" height="12" rx="2" fill="var(--icon-blue)"/></svg>
        socialhub.com/BramwellGarden
      </p>
      <p class="contact-line contact-line--small">
        <svg width="12" height="12" viewBox="0 0 12 12" aria-hidden="true"><rect width="12" height="12" rx="2" fill="var(--icon-blue)"/></svg>
        chirper.com/BramwellGarden
      </p>
      <p class="contact__abn">ABN: XXX XXX XXX</p>
    </div>
  </section>

</div>
</body>
</html>
```